High End Business Card Design for Flooring Store

Looking for a new card design for our hardwood flooring company. We have no print budget for these and are open to cards made from wood, metal, cardstock with embossed print ... or any combination of these. No plastic.

We sell luxury products and I want the cards to reflect our image of quality and class.

Our contact information as such;
Employee Name
418 Calloway Blvd.
Harrowfield, ON
E3K-2P8
(555) 314-2968
Employee email @brantelfloors.com

Target Market(s)

Home Builders

Contact Information for Business Card

Emnployee name, business contact information

```html
<!DOCTYPE html>
<html lang="en">
<head>
<meta charset="UTF-8">
<title>Brantel Business Card</title>
<link rel="stylesheet" href="https://fonts.googleapis.com/css2?family=Montserrat:wght@400;500&family=Outfit:wght@400;600&display=swap">
<style>
  :root {
    --backdrop: #6e7174;
    --card-dark: #1f1f1f;
    --card-light: #ffffff;
    --brand-red: #962b24;
    --accent-gold: #f3d892;
    --ink: #1d1d1d;
    --muted: #6b6b6b;
    --white: #ffffff;
  }
  * { margin: 0; padding: 0; box-sizing: border-box; }
  html, body { width: 1200px; height: 1200px; overflow: hidden; }
  body {
    background: var(--backdrop);
    position: relative;
    font-family: "Outfit", sans-serif;
  }
  .card {
    position: absolute;
    left: 245px;
    width: 709px;
    height: 410px;
    overflow: hidden;
  }
  .card--front { top: 130px; background: var(--card-dark); }
  .card--back { top: 643px; background: var(--card-light); }

  /* Front */
  .front-brand {
    position: absolute;
    top: 130px;
    left: 0;
    width: 100%;
    text-align: center;
  }
  .front-brand__name {
    font-family: "Montserrat", sans-serif;
    font-weight: 400;
    font-size: 92px;
    line-height: 1;
    color: var(--brand-red);
    letter-spacing: 1px;
  }
  .front-brand__tagline {
    margin-top: 6px;
    font-family: "Montserrat", sans-serif;
    font-weight: 500;
    font-size: 22px;
    line-height: 25px;
    color: var(--white);
  }

  /* Back */
  .back-accent {
    position: absolute;
    inset: 0;
    width: 709px;
    height: 410px;
  }
  .back-brand {
    position: absolute;
    top: 40px;
    left: 60px;
    text-align: center;
  }
  .back-brand__name {
    font-family: "Montserrat", sans-serif;
    font-weight: 400;
    font-size: 46px;
    line-height: 1;
    color: var(--brand-red);
  }
  .back-brand__tagline {
    margin-top: 3px;
    font-family: "Montserrat", sans-serif;
    font-size: 12.5px;
    line-height: 13.5px;
    color: var(--muted);
  }
  .holder {
    position: absolute;
    left: 49px;
    top: 257px;
  }
  .holder__name {
    font-weight: 600;
    font-size: 24px;
    letter-spacing: 1.2px;
    color: var(--brand-red);
    line-height: 1.1;
  }
  .holder__role {
    font-size: 16px;
    letter-spacing: 0.5px;
    color: var(--ink);
    margin-top: 1px;
  }
  .divider {
    position: absolute;
    left: 49px;
    top: 313px;
    width: 617px;
    height: 1px;
    background: var(--ink);
  }
  .contact {
    position: absolute;
    top: 330px;
    list-style: none;
    font-size: 16px;
    color: var(--ink);
  }
  .contact li {
    display: flex;
    align-items: center;
    gap: 10px;
    height: 25px;
  }
  .contact--left { left: 50px; }
  .contact--right { right: 44px; }
  .contact--right li { justify-content: flex-end; }
  .contact svg { width: 15px; height: 15px; fill: var(--brand-red); flex: none; }
</style>
</head>
<body>

<section class="card card--front">
  <div class="front-brand">
    <div class="front-brand__name">Brantel</div>
    <div class="front-brand__tagline">Bois Franc &amp; Marches<br>Floors &amp; Staircases</div>
  </div>
</section>

<section class="card card--back">
  <svg class="back-accent" viewBox="0 0 709 410" role="img" aria-label="Pale gold decorative corner shape">
    <polygon points="445,95 565,0 709,0 709,410 640,410 437,233 510,155" fill="var(--accent-gold)"/>
  </svg>

  <div class="back-brand">
    <div class="back-brand__name">Brantel</div>
    <div class="back-brand__tagline">Bois Franc &amp; Marches<br>Floors &amp; Staircases</div>
  </div>

  <div class="holder">
    <div class="holder__name">Julien Arsenault</div>
    <div class="holder__role">Manager</div>
  </div>

  <div class="divider"></div>

  <ul class="contact contact--left">
    <li>
      <svg viewBox="0 0 24 24"><path d="M9 2 L12 7 L9.5 9.5 Q11 15 14.5 17 L17 14.5 L21 18 L18 22 Q6 20 5 6 Z"/></svg>
      <span>(555)314-2968</span>
    </li>
    <li>
      <svg viewBox="0 0 24 24"><path d="M2 5 H22 V19 H2 Z" fill="var(--brand-red)"/><path d="M3.5 6.5 L12 13 L20.5 6.5" stroke="#fff" stroke-width="1.5" fill="none"/></svg>
      <span>Info@brantelfloors.com</span>
    </li>
  </ul>

  <ul class="contact contact--right">
    <li>
      <span>www.brantelfloors.com</span>
      <svg viewBox="0 0 24 24"><circle cx="12" cy="12" r="10"/><path d="M2 12 H22 M12 2 V22 M12 2 Q6 12 12 22 M12 2 Q18 12 12 22" stroke="#fff" stroke-width="1.4" fill="none"/></svg>
    </li>
    <li>
      <span>418 Calloway Blvd. Harrowfield, ON E3K 2P8</span>
      <svg viewBox="0 0 24 24"><path d="M12 1 C7 1 4 5 4 9 C4 15 12 23 12 23 C12 23 20 15 20 9 C20 5 17 1 12 1 Z M12 5.5 A3.5 3.5 0 1 0 12 12.5 A3.5 3.5 0 1 0 12 5.5 Z" fill-rule="evenodd"/></svg>
    </li>
  </ul>
</section>

</body>
</html>
```